Letterhead for NZ School promoting centennial celebrations

Our local Primary School (grade school) is turning 100 in 2014 and we would like the letterhead to be updated and incorporate the words "Celebrating 100yrs in 2014" to start creating a bit of interest.
The schools name is Rawa Kōtuku, which is Maori for 'the stitchbird'. The school is quintessential rural new zealand, but very close to Auckland city and is well patronised. The colours of the school are white, maroon and yellow, but predominantly maroon. The emblem/logo is on the existing letterhead and will need some work as it is of rather poor quality. It is of the Hihi (stitchbird) perched on a Kowhai branch. The winning design could lead to work in further updating of the emblem.
We would like the letterhead to be modernised, but not to the point where you wouldn't think it was for a rural nz school, if that makes sense!

Thanks for all your ideas so far. A couple of pointers: the footer space would be best left empty as we may use this area to put sponsors names - If you are using a watermark would prefer just the bird and no extra colour with it - The ones that are standing out at the moment are flowy (?) modern, not too clunky, busy or boxy. Thanks again.

Forgot to mention we would also now like the dates for the event on there which are
7-9 March
Thanks, Gordon.

Industry/Entity Type

School

Requirements
Must have
• Rawa Kōtuku Primary School
'Celebrating 100yrs in 2014'
school motto: HONOUR – RESPECT – DILIGENCE
TELEPHONE 09-418-5531
FAX 09-418-5532
office@rawakotuku.example.nz
and must have the school emblem
Should not have
• Not too much background colour, as I believe the school prints it's own paper. But this is really only a guideline, if it looks good I'm flexible.
I don't think it should have colours other than maroon, white, yellow and black, but realising that is fairly rough palette will be open to a splash of something else if it works better.
The writing below the bird could be removed also.

```html
<!DOCTYPE html>
<html lang="en">
<head>
<meta charset="utf-8">
<title>Rawa Kōtuku Primary School – Letterhead</title>
<link rel="stylesheet" href="https://fonts.googleapis.com/css2?family=Tinos:wght@700&family=Arimo:wght@700&family=Jost:ital,wght@1,600;1,700&display=swap">
<style>
  :root {
    --maroon: #8e1b3c;
    --sun: #f4ca24;
    --sun-soft: #f8dd82;
    --cream: #fcf2d2;
    --cream-deep: #f7e7b4;
    --paper: #ffffff;
    --contact: #f5d98a;
  }
  html, body {
    margin: 0;
    padding: 0;
    overflow: hidden;
    background: var(--paper);
  }
  .letterhead {
    position: relative;
    width: 929px;
    height: 1200px;
    overflow: hidden;
    background: var(--cream);
  }
  .letterhead__shapes {
    position: absolute;
    inset: 0;
    width: 929px;
    height: 1200px;
  }
  .school-name,
  .school-motto,
  .contact-line,
  .centennial {
    position: absolute;
    margin: 0;
    white-space: nowrap;
    transform-origin: left bottom;
  }
  .school-name {
    left: 198px;
    top: 112px;
    font-family: "Tinos", "Times New Roman", serif;
    font-weight: 700;
    font-size: 35px;
    color: var(--maroon);
    transform: rotate(-11deg);
  }
  .school-motto {
    left: 204px;
    top: 158px;
    font-family: "Arimo", Arial, sans-serif;
    font-weight: 700;
    font-size: 12px;
    letter-spacing: 0.2px;
    color: var(--paper);
    transform: rotate(-8deg);
  }
  .contact-line {
    left: 472px;
    top: 206px;
    font-family: "Jost", "Futura", sans-serif;
    font-style: italic;
    font-weight: 600;
    font-size: 13px;
    color: var(--contact);
    transform: rotate(9.3deg);
  }
  .centennial {
    left: 34px;
    top: 960px;
    font-family: "Jost", "Futura", sans-serif;
    font-style: italic;
    font-weight: 700;
    font-size: 43px;
    line-height: 46px;
    color: var(--cream-deep);
    transform: rotate(7.5deg);
  }
  .centennial span { display: block; }
</style>
</head>
<body>
<main class="letterhead">
  <svg class="letterhead__shapes" viewBox="0 0 929 1200" aria-hidden="true">
    <!-- writing area -->
    <path fill="var(--paper)" d="M0 380 C 20 300, 70 240, 170 222 L 520 205 C 650 215, 800 250, 929 292 L 929 1112 C 650 1100, 300 1040, 0 975 Z"/>
    <!-- header bands -->
    <path fill="var(--sun-soft)" d="M0 0 H 860 C 790 110, 560 190, 380 212 L 0 240 Z"/>
    <path fill="var(--sun)" d="M0 0 H 752 C 690 90, 480 170, 0 222 Z"/>
    <!-- emblem placeholder -->
    <circle cx="128" cy="132" r="44" fill="var(--maroon)"/>
  </svg>

  <h1 class="school-name">Rawa Kōtuku Primary School</h1>
  <p class="school-motto">HONOUR – RESPECT – DILIGENCE</p>
  <p class="contact-line">ph 09-418-5531 | fax 09-418-5532 | office@rawakotuku.example.nz</p>
  <p class="centennial"><span>Celebrating 100yrs in 2014</span><span>7-9 March</span></p>
</main>
</body>
</html>
```